Website Wordpress Responsive Design and Development - Landscape Company

Site is currently under construction, but the old site needs a refresh.
Need a fully responsive wordpress website (built in Elementor or comparable theme).
Here's the way it looked prior :
https://pastpages.example/snap/20220330041341/http://brookmoorgreens.example/
Their current designer came up with a website sample and it looks terrible :
https://talkowenpics.sitebuild.example/mysite/projects
Websites the client likes for some inspiration, but needs better than these :
https://www.quarrinbeckgroundworkers.example/
http://kvatelierpx.example/
https://tullidgepartners.example/
https://www.garbettcoinc.example/

Navigation includes :
• Home
• Complete structure of website content is available in the home page, yielding main information on services.
• Visually appealing but simple to use and navigate. Subtle amount of content, but enough for search engines to be able to read up the target phrases.
• Sections on the home page include :
▪ About - Information about the company and main service focus
▪ Gallery - Imagery categorized to include lightbox style zoom.
▪ Contact - Contact details and connection information
• About
• Bannered header
• Content appropriately formatted to subject
• Gallery
• Bannered header
• Each of the albums would have their own categorized image content
• Contact
• Bannered header
• Social Media connector available on all pages (like box, feed, etc) if applicable
• Content can be updated on all pages
• Basic Optimization for SEO with title tags, meta data where applicable.
• Google Analytics and Sitemap installed. (google account will be provided)
• Google Business Listing and Search Console Accounts created

Coded - Design and coding required

1 page

• Wordpress Responsive Design

```html
<!DOCTYPE html>
<html lang="en">
<head>
<meta charset="utf-8">
<title>Brookmoor Greens – Landscape Construction &amp; Maintenance</title>
<link href="https://fonts.googleapis.com/css2?family=Roboto:wght@400;500;700&family=Ubuntu:wght@500;700&display=swap" rel="stylesheet">
<style>
:root{
  --green:#2f6a07;
  --green-dark:#24540a;
  --green-mid:#3f7d14;
  --ink:#222;
  --grey:#8a8a8a;
  --band:#f2f2f2;
  --footer:#232323;
  --white:#fff;
}
*{box-sizing:border-box;margin:0;padding:0}
html,body{width:1200px;height:3599px;overflow:hidden}
body{position:relative;font-family:"Roboto",sans-serif;color:var(--ink);background:var(--white)}
.abs{position:absolute}
.heading{font-family:"Ubuntu",sans-serif;font-weight:500;text-transform:uppercase;letter-spacing:.5px}
.heading .accent{color:var(--green)}
.btn{display:flex;align-items:center;justify-content:center;background:var(--green);color:var(--white);font-weight:700;font-size:15px;border-radius:30px;text-transform:uppercase}

/* header */
.site-header{left:0;top:0;width:1200px;height:102px;background:var(--white);z-index:5}
.brand{font-family:"Ubuntu",sans-serif;font-weight:500;font-size:28px;color:var(--green);left:112px;top:35px}
.main-nav{left:440px;top:46px;display:flex;gap:25px;font-size:13.5px;font-weight:500}
.main-nav a{color:var(--ink);text-decoration:none}
.main-nav a.current{color:var(--green)}
.social{display:flex;gap:10px}
.social span{width:36px;height:36px;background:var(--white);box-shadow:0 2px 6px rgba(0,0,0,.15);display:block}
.social span.on{background:var(--green)}
.header-social{left:750px;top:36px}
.header-phone{left:954px;top:0;width:246px;height:102px;background:var(--green);color:var(--white);font-size:20px;font-weight:500;display:flex;align-items:center;justify-content:center}

/* hero */
.hero-photo{left:0;top:102px;width:1200px;height:640px;background:linear-gradient(180deg,#b9cde0 0%,#9fb78a 30%,#5f9a2c 55%,#6fa82e 80%,#7eb23a 100%)}
.hero-panel{left:650px;top:225px;width:438px;height:275px;background:rgba(255,255,255,.78);padding:36px 42px}
.hero-panel h1{font-family:"Ubuntu",sans-serif;font-weight:500;font-size:39px;color:var(--green)}
.hero-panel p{font-size:17px;line-height:29px;margin-top:14px;color:#2a2a2a}
.hero-panel .btn{width:155px;height:49px;margin-top:26px}
.slide-arrow{width:36px;height:36px;border-radius:50%;background:var(--white);top:345px;display:flex;align-items:center;justify-content:center}
.hero-wave{left:0;top:560px}
.scroll-down{left:555px;top:623px;width:90px;height:90px;border-radius:50%;background:var(--white);box-shadow:0 4px 10px rgba(0,0,0,.15);display:flex;align-items:center;justify-content:center}

/* about */
.about-title{left:112px;top:810px;font-size:39px;color:var(--ink)}
.about-text{left:112px;top:884px;width:488px;font-size:13.5px;line-height:25.7px;color:var(--grey);text-align:justify}
.about-text b{color:var(--ink);font-weight:500}
.about-text p+p{margin-top:11px}
.about-btn{left:112px;top:1108px;width:145px;height:49px}
.about-photo{left:659px;top:760px;width:430px;height:410px;border-radius:50%;background:radial-gradient(circle at 40% 30%,#9cc6ec 0%,#7fb0d6 30%,#6d9d3c 55%,#4e7f24 80%,#a69f8c 100%)}
.about-ring{left:650px;top:755px}

/* services */
.services{left:0;top:1273px;width:1200px;height:591px;background:var(--band)}
.section-title{width:1200px;left:0;text-align:center;font-size:45px}
.card{border:4px solid var(--white);box-shadow:0 3px 10px rgba(0,0,0,.18);overflow:hidden}
.service-card{top:1437px;width:303px;height:354px;display:flex;flex-direction:column;align-items:center;justify-content:flex-end;padding-bottom:22px;color:var(--white);font-weight:700;font-size:20px}
.service-card .label{margin-top:10px;text-shadow:0 1px 3px rgba(0,0,0,.5)}

/* projects */
.project{width:469px}
.project-row2{top:2365px;width:303px;height:250px}
.project-hover{display:flex;align-items:center;justify-content:center;color:var(--white);font-weight:700;font-size:19px}

/* contact */
.contact{left:0;top:2726px;width:1200px;height:560px;background:linear-gradient(180deg,#2c6a08 0%,#2f6e0b 60%,#285f08 100%)}
.contact-title{color:var(--white);top:2787px;font-size:41px}
.field{background:var(--white);border-radius:3px;font-size:14.5px;color:#8b8b8b;padding:14px 17px}
.send-btn{left:516px;top:3030px;width:169px;height:48px;background:#262626;color:var(--white);font-weight:700;font-size:14.5px;border-radius:30px;display:flex;align-items:center;justify-content:center}
.contact-wave{left:0;top:3120px}

/* footer */
.site-footer{left:0;top:3270px;width:1200px;height:329px;background:var(--footer)}
.footer-brand{width:1200px;left:0;top:3298px;text-align:center;font-family:"Ubuntu",sans-serif;font-weight:500;font-size:28px;color:var(--green-mid)}
.footer-nav{width:1200px;left:0;top:3357px;display:flex;justify-content:center;gap:32px;color:var(--white);font-weight:700;font-size:16px}
.rule{height:1px;background:#444}
.info{display:flex;gap:24px;align-items:center;color:#cfcfcf;font-size:13px;line-height:20px}
.info .dot{width:76px;height:76px;border-radius:50%;background:var(--green);display:flex;align-items:center;justify-content:center;flex:none}
.info strong{color:var(--white);font-size:14px;display:block;margin-bottom:4px}
.divider{width:1px;height:104px;background:#444;top:3418px}
.copyright{left:0;width:1200px;top:3556px;text-align:center;color:var(--white);font-size:12px}
.footer-social{left:914px;top:3546px}
</style>
</head>
<body>

<header class="site-header abs">
  <div class="brand abs">Brookmoor Greens</div>
  <nav class="main-nav abs">
    <a class="current" href="#">HOME</a><a href="#">ABOUT</a><a href="#">GALLERY</a><a href="#">CONTACT</a>
  </nav>
  <div class="social header-social abs" aria-label="Social links">
    <span class="on"></span><span></span><span></span><span></span>
  </div>
  <div class="header-phone abs">(555) 014-2290</div>
</header>

<section class="hero">
  <div class="hero-photo abs" role="img" aria-label="Landscaped park with lawn, flower beds, street lamp and curving brick path"></div>
  <div class="hero-panel abs">
    <h1>Brookmoor Greens</h1>
    <p>Brookmoor Greens is a full service landscape construction &amp; maintenance company.</p>
    <div class="btn">Get Started</div>
  </div>
  <div class="slide-arrow abs" style="left:41px"><svg width="14" height="14" viewBox="0 0 14 14"><path d="M9 2 4 7l5 5" fill="none" stroke="#222" stroke-width="2"/></svg></div>
  <div class="slide-arrow abs" style="left:1122px"><svg width="14" height="14" viewBox="0 0 14 14"><path d="M5 2l5 5-5 5" fill="none" stroke="#222" stroke-width="2"/></svg></div>
  <svg class="hero-wave abs" width="1200" height="190" viewBox="0 0 1200 190">
    <path d="M0 50 C120 150 300 180 470 160 C640 140 760 60 960 30 C1080 15 1160 25 1200 40 L1200 190 L0 190Z" fill="#fff"/>
    <path d="M560 150 C700 110 820 40 980 25 C1080 18 1160 40 1200 60 L1200 20 C1150 0 1060 -8 960 5 C820 25 700 95 560 150Z" fill="var(--green)"/>
    <path d="M0 95 C140 160 330 175 520 150" fill="none" stroke="var(--green)" stroke-width="3"/>
  </svg>
  <div class="scroll-down abs"><svg width="30" height="20" viewBox="0 0 30 20"><path d="M3 4l12 12L27 4" fill="none" stroke="var(--green)" stroke-width="3"/></svg></div>
</section>

<section class="about">
  <h2 class="about-title heading abs"><span class="accent">About</span> Us</h2>
  <div class="about-text abs">
    <p><b>Brookmoor Greens</b> is a full service landscape construction and maintenance company. We have been servicing the community for over 20 years and in that time have established ourselves as a premier contractor in the East End. We pride ourselves on quality work and excellent customer service.</p>
    <p>Sed dolore laboris nisi ut aliquip ex ea commodo consequat duis aute irure dolor in reprehenderit in voluptate velit esse cillum dolore eu fugiat nulla pariuip ex ea commodo conesse cillum dolore eu fugisatur.</p>
  </div>
  <div class="about-btn btn abs">Learn More</div>
  <div class="about-photo abs" role="img" aria-label="Backyard garden with stone path, patio seating and house"></div>
  <svg class="about-ring abs" width="450" height="420" viewBox="0 0 450 420"><path d="M250 8 A205 205 0 0 1 310 402" fill="none" stroke="#fff" stroke-width="4"/></svg>
</section>

<section class="services abs"></section>
<h2 class="section-title heading abs" style="top:1333px"><span class="accent">Our</span> Services</h2>
<div class="service-card card abs" style="left:115px;background:linear-gradient(180deg,#4b5a3e 0%,#6aa22b 30%,#5c8f2a 60%,#7f7f78 100%)" role="img" aria-label="Lawn with paved walkway and stepping stones">
  <svg width="46" height="40" viewBox="0 0 46 40" fill="none" stroke="#fff" stroke-width="2"><path d="M4 38h38M10 38V20l13-10 13 10v18M19 38v-9h8v9"/></svg>
  <div class="label">LANDSCAPING</div>
</div>
<div class="service-card card abs" style="left:448px;background:linear-gradient(180deg,#5f8a3c 0%,#3c8a92 35%,#4f6b3a 65%,#3f4a48 100%)" role="img" aria-label="Gardener planting shrubs">
  <svg width="42" height="42" viewBox="0 0 42 42" fill="none" stroke="#fff" stroke-width="2"><circle cx="21" cy="21" r="8"/><circle cx="21" cy="21" r="16" stroke-dasharray="5 4"/></svg>
  <div class="label">MAINTENANCE</div>
</div>
<div class="service-card card abs" style="left:782px;background:linear-gradient(180deg,#5c7f43 0%,#769a3c 40%,#a39a4f 70%,#8c8470 100%)" role="img" aria-label="Terraced flower beds with stone walls">
  <svg width="44" height="44" viewBox="0 0 44 44" fill="none" stroke="#fff" stroke-width="2"><circle cx="22" cy="22" r="5"/><circle cx="22" cy="10" r="7"/><circle cx="22" cy="34" r="7"/><circle cx="10" cy="22" r="7"/><circle cx="34" cy="22" r="7"/></svg>
  <div class="label">FLOWERS</div>
</div>

<h2 class="section-title heading abs" style="top:1950px"><span class="accent">Featured</span> Projects</h2>
<div class="project card abs" style="left:115px;top:2044px;height:292px;background:linear-gradient(180deg,#8eaed3 0%,#d7d0b4 35%,#4f7d2a 60%,#a9a9a3 100%)" role="img" aria-label="Large house with gravel driveway and evergreens"></div>
<div class="project card project-hover abs" style="left:616px;top:2044px;height:292px;background:linear-gradient(180deg,#3b4235 0%,#3f4a36 50%,#354a25 100%)" role="img" aria-label="Brick mill building behind a large tree, darkened on hover">OLD MILL HARBOR LANE</div>
<div class="project card project-row2 abs" style="left:115px;background:linear-gradient(180deg,#c9d6e4 0%,#6e8f52 40%,#4f7f2a 75%,#5d4d7a 100%)" role="img" aria-label="Shingle style home with lawn and purple flowers"></div>
<div class="project card project-row2 abs" style="left:448px;background:linear-gradient(180deg,#5b9ad8 0%,#e3e3e0 40%,#6d8c4b 65%,#9fbf7a 100%)" role="img" aria-label="Modern house with grass paver driveway"></div>
<div class="project card project-row2 abs" style="left:782px;background:linear-gradient(180deg,#cbd3dd 0%,#b3825e 35%,#4f7f22 65%,#3f6a1c 100%)" role="img" aria-label="Villa with clipped boxwood parterre garden"></div>

<section class="contact abs" role="img" aria-label="Green tinted garden background"></section>
<h2 class="section-title heading contact-title abs">Contact Us</h2>
<div class="field abs" style="left:165px;top:2862px;width:282px;height:49px">Full Name</div>
<div class="field abs" style="left:458px;top:2862px;width:282px;height:49px">Phone</div>
<div class="field abs" style="left:752px;top:2862px;width:282px;height:49px">Email Address</div>
<div class="field abs" style="left:165px;top:2923px;width:869px;height:93px">Message</div>
<div class="send-btn abs">SEND MESSAGE</div>
<svg class="contact-wave abs" width="1200" height="160" viewBox="0 0 1200 160">
  <path d="M0 70 C120 150 260 150 420 110 C640 50 900 0 1200 70 L1200 160 L0 160Z" fill="#fff"/>
  <path d="M0 110 C140 180 300 170 460 125 C680 60 940 30 1200 110 L1200 160 L0 160Z" fill="var(--footer)"/>
</svg>

<footer class="site-footer abs"></footer>
<div class="footer-brand abs">Brookmoor Greens</div>
<nav class="footer-nav abs"><span>HOME</span><span>/</span><span>ABOUT</span><span>/</span><span>GALLERY</span><span>/</span><span>CONTACT</span></nav>
<div class="rule abs" style="left:112px;top:3402px;width:975px"></div>
<div class="info abs" style="left:112px;top:3428px">
  <div class="dot"><svg width="30" height="34" viewBox="0 0 30 34" fill="none" stroke="#fff" stroke-width="2.5"><path d="M15 30S5 19 5 12a10 10 0 0 1 20 0c0 7-10 18-10 18z"/><circle cx="15" cy="12" r="3.5"/></svg></div>
  <div><strong>LOCATION:</strong>P.O. Box 318<br>Westhollow, NY 10998</div>
</div>
<div class="divider abs" style="left:425px"></div>
<div class="info abs" style="left:505px;top:3428px">
  <div class="dot"><svg width="30" height="30" viewBox="0 0 30 30" fill="#fff"><path d="M8 3l5 6-3 3c1 3 5 7 8 8l3-3 6 5-3 5C14 27 3 16 3 6z"/></svg></div>
  <div><strong>PHONE:</strong>(555) 014-2290</div>
</div>
<div class="divider abs" style="left:775px"></div>
<div class="info abs" style="left:825px;top:3428px">
  <div class="dot"><svg width="32" height="26" viewBox="0 0 32 26" fill="none" stroke="#fff" stroke-width="2.5"><rect x="2" y="2" width="28" height="22" rx="2"/><path d="M2 4l14 11L30 4"/></svg></div>
  <div><strong>EMAIL:</strong>hello@brookmoorgreens.example</div>
</div>
<div class="rule abs" style="left:112px;top:3540px;width:975px"></div>
<div class="copyright abs">© 2022 Brookmoor Greens &nbsp;|&nbsp; All Rights Reserved</div>
<div class="social footer-social abs" aria-label="Social links">
  <span class="on"></span><span></span><span></span><span></span>
</div>

</body>
</html>
```